Redesign and move to Wordpress for quarvendo.com

Our website needs a redesign and at the same time we are moving it to Wordpress. Please help us with a new digital professional look and feel.

We are an Australian Software Engineering company specialising in advanced software development using in A.I., PLatform Engineering, Integration and Cloud. See the current quarvendo.com for more information about us.

```html
<!DOCTYPE html>
<html lang="en">
<head>
<meta charset="utf-8">
<title>Quarvendo — Reliable Smart Software Engineering</title>
<link rel="stylesheet" href="https://fonts.googleapis.com/css2?family=League+Spartan:wght@700;800&family=Poppins:wght@400;500;600&family=Jost:wght@400;500;600&display=swap">
<style>
:root{
  --brand-blue:#1b5fa3;
  --header-blue:#1a5d9f;
  --footer-blue:#1b62a7;
  --teal:#4cbfba;
  --navy:#0c2b46;
  --cream:#fbfcf1;
  --ink:#2b2b2b;
  --heading-blue:#1c5aa0;
  --panel:#f1f1f1;
  --white:#ffffff;
}
*{box-sizing:border-box;margin:0;padding:0}
html,body{width:1200px;height:3125px;overflow:hidden;background:var(--white)}
body{font-family:"Poppins",sans-serif;color:var(--ink);position:relative}
.site{position:absolute;left:151px;top:200px;width:897px;height:2842px;box-shadow:0 12px 40px rgba(0,0,0,.25);overflow:hidden;background:var(--cream)}
.abs{position:absolute}
.btn{position:absolute;background:var(--teal);color:var(--white);font-family:"Jost",sans-serif;font-weight:500;font-size:11px;letter-spacing:.3px;display:flex;align-items:center;justify-content:center;gap:5px;text-transform:uppercase}
.btn .dot{width:9px;height:9px;border-radius:50%;background:var(--white);position:relative}
.btn .dot::after{content:"";position:absolute;left:3px;top:2.5px;border-left:4px solid var(--teal);border-top:2px solid transparent;border-bottom:2px solid transparent}

/* header */
.site-header{position:absolute;left:0;top:0;width:897px;height:58px;background:var(--header-blue)}
.brand{position:absolute;display:flex;align-items:center;gap:10px;color:var(--white);font-family:"Jost",sans-serif;font-weight:400}
.brand .mark{border:2px solid var(--white)}
.main-nav{position:absolute;left:322px;top:21px;display:flex;font-family:"Jost",sans-serif;font-weight:500;font-size:11px;color:var(--white);gap:0}
.main-nav span{padding:0 12px;border-left:1px solid rgba(255,255,255,.7);line-height:14px}
.main-nav span:first-child{border-left:none;color:var(--teal)}

/* hero */
.hero{position:absolute;left:0;top:58px;width:897px;height:512px;background:linear-gradient(160deg,#4a7cb6 0%,#2d5f9b 45%,#1f4d88 100%)}
.hero-title{position:absolute;left:0;top:156px;width:897px;text-align:center;font-family:"League Spartan",sans-serif;font-weight:800;font-size:66px;line-height:72px;color:var(--white)}
.hero .btn{left:370px;top:316px;width:157px;height:39px}

/* about */
.photo-frame{position:absolute;padding:9px}
.photo-frame .fill{width:100%;height:100%}
.about-title{position:absolute;left:480px;top:680px;font-family:"League Spartan",sans-serif;font-weight:800;font-size:30px;color:var(--heading-blue);letter-spacing:.5px}
.about-text{position:absolute;left:480px;top:724px;width:384px;font-size:10.5px;line-height:18.5px;text-align:justify;color:#333}
.client-badge{position:absolute;top:900px;width:62px;height:56px;background:var(--white);border-radius:4px}
.client-badge i{position:absolute;left:16px;top:17px;width:30px;height:22px;background:#3a3a3a;border-radius:3px}

/* services */
.services{position:absolute;left:0;top:1090px;width:897px;height:610px;background:var(--navy)}
.section-title{position:absolute;font-family:"League Spartan",sans-serif;font-weight:800;font-size:30px;color:var(--white);letter-spacing:.5px;text-align:center}
.card{position:absolute;width:175px;border:1px solid var(--teal);border-radius:6px;color:var(--white);text-align:center;font-family:"Jost",sans-serif;font-weight:600;font-size:11px}
.card .label{position:absolute;left:0;width:100%}
.card .go{position:absolute;left:73px;width:29px;height:29px;border-radius:50%;background:var(--teal)}
.go svg{position:absolute;left:6px;top:6px}
.dots{position:absolute;display:flex;gap:9px}
.dots b{width:7px;height:7px;border-radius:50%;background:#5d7184}
.dots b.on{background:var(--teal)}
.slider-arrow{position:absolute;color:var(--teal);font-size:16px;font-family:"Jost",sans-serif}

/* news */
.news-title{position:absolute;left:0;top:1748px;width:897px;text-align:center;font-family:"League Spartan",sans-serif;font-weight:800;font-size:30px;color:var(--heading-blue);letter-spacing:.5px}
.article{position:absolute;top:1816px;width:177px;text-align:center}
.article .thumb{width:177px;height:176px}
.article p{margin-top:12px;font-family:"Jost",sans-serif;font-size:9.5px;line-height:12px;color:#333;padding:0 4px}
.article svg{margin-top:10px}

/* meet */
.meet{position:absolute;left:0;top:2132px;width:897px;height:423px;background:var(--navy)}
.booking{position:absolute;left:448px;top:2220px;width:416px;height:244px;background:var(--panel)}
.booking .k{position:absolute;font-family:"Jost",sans-serif;font-size:9px;font-weight:600;color:var(--teal)}
.booking .sel{position:absolute;height:20px;background:var(--white);border:1px solid #bdbdbd;border-radius:2px;font-family:"Jost",sans-serif;font-size:9px;color:#444;padding:4px 6px}
.booking .sel::after{content:"";position:absolute;right:5px;top:7px;border-top:4px solid #444;border-left:3px solid transparent;border-right:3px solid transparent}
.booking .sel.date::after{display:none}
.booking .sel.date{color:#999}
.tick{position:absolute;top:2353px;width:15px;height:15px;border-radius:50%;background:var(--teal)}
.tick svg{position:absolute;left:3px;top:3px}

/* footer */
.site-footer{position:absolute;left:0;top:2555px;width:897px;height:287px;background:var(--footer-blue);color:var(--white)}
.footer-nav{position:absolute;top:2678px;left:0;width:897px;display:flex;justify-content:center;gap:26px;font-family:"Jost",sans-serif;font-weight:500;font-size:11px;color:var(--white)}
.footer-nav span:first-child{color:var(--teal)}
.social{position:absolute;top:2721px;width:14px;height:14px;border-radius:50%;border:2px solid var(--teal)}
.copyright{position:absolute;top:2760px;left:0;width:897px;text-align:center;font-family:"Jost",sans-serif;font-size:10px;color:var(--white)}
</style>
</head>
<body>
<div class="site">

  <header class="site-header">
    <div class="brand" style="left:37px;top:11px;font-size:30px;line-height:36px">
      <span class="mark" style="width:34px;height:34px;display:block"></span>quarvendo
    </div>
    <nav class="main-nav"><span>HOME</span><span>ABOUT</span><span>SERVICES</span><span>BLOGS</span><span>CONTACT</span></nav>
    <div class="btn" style="left:662px;top:11px;width:165px;height:36px">Free Consultation <span class="dot"></span></div>
  </header>

  <section class="hero">
    <div class="abs" role="img" aria-label="Engineers working at a desk overlaid with a blue holographic data interface" style="inset:0;background:linear-gradient(180deg,rgba(120,160,210,.35),rgba(20,60,120,.25))"></div>
    <h1 class="hero-title">Reliable Smart<br>Software Engineering</h1>
    <div class="btn">Get Started Now <span class="dot"></span></div>
  </section>

  <!-- about -->
  <div class="photo-frame" style="left:42px;top:627px;width:182px;height:123px;background:var(--brand-blue)"><div class="fill" role="img" aria-label="Laptop showing an AI chip graphic" style="background:linear-gradient(135deg,#d9dde6,#5b4a8a 55%,#c9ced8)"></div></div>
  <div class="photo-frame" style="left:254px;top:627px;width:184px;height:249px;background:var(--brand-blue)"><div class="fill" role="img" aria-label="Two colleagues reviewing a tablet in a modern office" style="background:linear-gradient(160deg,#c7cdd3,#8a6f5e 50%,#3d5d83)"></div></div>
  <div class="photo-frame" style="left:42px;top:784px;width:182px;height:246px;background:var(--teal)"><div class="fill" role="img" aria-label="Professional working at a holographic touch table" style="background:linear-gradient(180deg,#5a5f66 0%,#2e3b52 45%,#1f5c9e 100%)"></div></div>
  <div class="photo-frame" style="left:254px;top:906px;width:184px;height:124px;background:var(--teal)"><div class="fill" role="img" aria-label="Person at a screen with an artificial intelligence interface in a dark room" style="background:linear-gradient(135deg,#0d1f4a,#2d4f9c 60%,#0e1a3c)"></div></div>

  <h2 class="about-title">ABOUT QUARVENDO</h2>
  <p class="about-text">At Quarvendo, we craft bespoke software solutions that are not available on the market. By building organizations market-leading products, process automation, legacy system enablement, or advanced intelligent systems, we empower our customers to achieve a competitive edge in their industry.</p>
  <div class="btn" style="left:480px;top:824px;width:126px;height:39px">Know More <span class="dot"></span></div>
  <div class="client-badge" style="left:500px"><i></i></div>
  <div class="client-badge" style="left:596px"><i></i></div>
  <div class="client-badge" style="left:692px"><i></i></div>
  <div class="client-badge" style="left:788px"><i></i></div>

  <!-- services -->
  <section class="services"></section>
  <div class="abs" role="img" aria-label="Developer at a desk with monitors showing IoT, robotics, big data and AI dashboards among plants" style="left:38px;top:1145px;width:264px;height:473px;border-radius:0 28px 0 0;background:linear-gradient(180deg,#e4e2dc 0%,#b9b7ae 35%,#2b5e93 60%,#5b5e62 100%)"></div>

  <h2 class="section-title" style="left:316px;top:1146px;width:541px">OUR SERVICES</h2>
  <div class="card" style="left:316px;top:1192px;height:178px">
    <svg class="abs" style="left:64px;top:8px" width="48" height="46" viewBox="0 0 48 46" fill="none" stroke="#fff" stroke-width="1.3"><circle cx="8" cy="5" r="4"/><circle cx="24" cy="5" r="4"/><circle cx="40" cy="5" r="4"/><circle cx="8" cy="23" r="4"/><circle cx="24" cy="23" r="4"/><circle cx="40" cy="23" r="4"/><circle cx="8" cy="41" r="4"/><circle cx="24" cy="41" r="4"/><circle cx="40" cy="41" r="4"/><path d="M12 23h8M28 23h8"/></svg>
    <div class="label" style="top:68px">ENTERPRISE Systems Integration</div>
    <div class="go" style="top:125px"><svg width="17" height="17" viewBox="0 0 17 17"><path d="M3 8.5h10M9 4.5l4 4-4 4" stroke="#0c2b46" stroke-width="2.4" fill="none"/></svg></div>
  </div>
  <div class="card" style="left:499px;top:1192px;height:178px">
    <svg class="abs" style="left:66px;top:6px" width="44" height="44" viewBox="0 0 44 44" fill="none" stroke="#fff" stroke-width="1.3"><circle cx="8" cy="8" r="3.5"/><circle cx="36" cy="6" r="3.5"/><circle cx="22" cy="20" r="4"/><circle cx="6" cy="36" r="3.5"/><circle cx="36" cy="34" r="3.5"/><path d="M11 10l8 7M33 8l-8 9M19 23l-10 10M25 23l8 9"/></svg>
    <div class="label" style="top:62px">Microservices</div>
    <div class="go" style="top:119px"><svg width="17" height="17" viewBox="0 0 17 17"><path d="M3 8.5h10M9 4.5l4 4-4 4" stroke="#0c2b46" stroke-width="2.4" fill="none"/></svg></div>
  </div>
  <div class="card" style="left:682px;top:1192px;height:178px">
    <div class="label" style="top:10px;font-size:9px;font-weight:500">glidely</div>
    <div class="label" style="top:36px">Glidely</div>
    <div class="go" style="top:93px"><svg width="17" height="17" viewBox="0 0 17 17"><path d="M3 8.5h10M9 4.5l4 4-4 4" stroke="#0c2b46" stroke-width="2.4" fill="none"/></svg></div>
  </div>
  <div class="slider-arrow" style="left:319px;top:1271px">‹</div>
  <div class="slider-arrow" style="left:844px;top:1271px">›</div>
  <div class="dots" style="left:522px;top:1378px"><b class="on"></b><b></b><b></b><b></b><b></b><b></b><b></b><b></b></div>

  <h2 class="section-title" style="left:316px;top:1399px;width:541px">OUR TECHNOLOGY EXPERTISE</h2>
  <div class="card" style="left:316px;top:1445px;height:181px">
    <div class="abs" style="left:64px;top:7px;width:48px;height:60px;background:#fff;border-radius:2px"></div>
    <div class="label" style="top:84px">Meridian Systems</div>
    <div class="go" style="top:132px"><svg width="17" height="17" viewBox="0 0 17 17"><path d="M3 8.5h10M9 4.5l4 4-4 4" stroke="#0c2b46" stroke-width="2.4" fill="none"/></svg></div>
  </div>
  <div class="card" style="left:499px;top:1445px;height:181px">
    <div class="abs" style="left:66px;top:7px;width:44px;height:44px;background:#2a7fd4;border-radius:3px"></div>
    <div class="label" style="top:70px">Cirrus Public Cloud Services</div>
    <div class="go" style="top:118px"><svg width="17" height="17" viewBox="0 0 17 17"><path d="M3 8.5h10M9 4.5l4 4-4 4" stroke="#0c2b46" stroke-width="2.4" fill="none"/></svg></div>
  </div>
  <div class="card" style="left:682px;top:1445px;height:181px">
    <div class="abs" style="left:63px;top:7px;width:48px;height:27px;background:#fff;border-radius:2px"></div>
    <div class="label" style="top:48px">Cirrus Pipelines</div>
    <div class="go" style="top:95px"><svg width="17" height="17" viewBox="0 0 17 17"><path d="M3 8.5h10M9 4.5l4 4-4 4" stroke="#0c2b46" stroke-width="2.4" fill="none"/></svg></div>
  </div>
  <div class="slider-arrow" style="left:319px;top:1525px">‹</div>
  <div class="slider-arrow" style="left:844px;top:1525px">›</div>
  <div class="dots" style="left:550px;top:1634px"><b></b><b></b><b class="on"></b><b></b><b></b></div>

  <!-- news -->
  <h2 class="news-title">NEWS &amp; ARTICLES</h2>
  <article class="article" style="left:50px">
    <div class="thumb" role="img" aria-label="Glowing server racks in a data centre" style="background:linear-gradient(180deg,#1c3b3a,#3e8f5b 45%,#d8f0c8 55%,#1e4b6e)"></div>
    <p>Why Most Upgrade Paths For LinkHub Lead To Using Cirrus Flow Apps</p>
    <svg width="16" height="14" viewBox="0 0 16 14"><path d="M1 7h12M8 2l5 5-5 5" stroke="#4cbfba" stroke-width="2" fill="none"/></svg>
  </article>
  <article class="article" style="left:259px">
    <div class="thumb" role="img" aria-label="Team meeting in front of a whiteboard showing an integration diagram" style="background:linear-gradient(160deg,#2b2b2b,#cfd2d6 45%,#5f6b7d 75%,#222)"></div>
    <p>Meet Quarvendo: The LinkHub Experts</p>
    <svg width="16" height="14" viewBox="0 0 16 14"><path d="M1 7h12M8 2l5 5-5 5" stroke="#4cbfba" stroke-width="2" fill="none"/></svg>
  </article>
  <article class="article" style="left:467px">
    <div class="thumb" role="img" aria-label="Monitor glowing with a golden network visualisation" style="background:linear-gradient(180deg,#1a2330,#6d5a2b 55%,#c9a252 80%,#2a2418)"></div>
    <p>How To Get Visibility Into Your LinkHub Environment</p>
    <svg width="16" height="14" viewBox="0 0 16 14"><path d="M1 7h12M8 2l5 5-5 5" stroke="#4cbfba" stroke-width="2" fill="none"/></svg>
  </article>
  <article class="article" style="left:676px">
    <div class="thumb" role="img" aria-label="Laptop displaying a security vulnerability report with charts" style="background:linear-gradient(180deg,#e6e6e8,#cfd0d4 45%,#555 70%,#dcdcdf)"></div>
    <p>Top 10 LinkHub Server Vulnerabilities And Security Recommendations</p>
    <svg width="16" height="14" viewBox="0 0 16 14"><path d="M1 7h12M8 2l5 5-5 5" stroke="#4cbfba" stroke-width="2" fill="none"/></svg>
  </article>

  <!-- meet -->
  <section class="meet"></section>
  <h2 class="section-title" style="left:56px;top:2183px;text-align:left">MEET WITH QUARVENDO</h2>
  <div class="abs" role="img" aria-label="Person on a video call with a consultant shown on a desktop monitor" style="left:32px;top:2228px;width:384px;height:275px;border-radius:26px 0 26px 0;background:linear-gradient(135deg,#e8e4dc,#8b7766 45%,#3b3b3d 70%,#d7d3cc)"></div>

  <div class="booking"></div>
  <div class="abs" style="left:470px;top:2246px;font-family:'Jost',sans-serif;font-size:9.5px;font-weight:600;color:#222">Please select service:</div>
  <div class="booking" style="background:none;pointer-events:none">
    <span class="k" style="left:22px;top:58px">Category</span>
    <span class="k" style="left:146px;top:58px">Service</span>
    <span class="k" style="left:270px;top:58px">Employee</span>
    <span class="sel" style="left:22px;top:74px;width:115px">Select category</span>
    <span class="sel" style="left:146px;top:74px;width:115px">Select service</span>
    <span class="sel" style="left:270px;top:74px;width:124px">Any</span>
    <span class="k" style="left:22px;top:113px">I'm available on or after</span>
    <span class="k" style="left:146px;top:113px;word-spacing:4px">Mon Tue Wed Thu Fri</span>
    <span class="k" style="left:264px;top:113px">Start from</span>
    <span class="k" style="left:333px;top:113px">Finish by</span>
    <span class="sel date" style="left:22px;top:130px;width:110px">January 17, 2025</span>
    <span class="sel" style="left:264px;top:130px;width:60px">8:00 am</span>
    <span class="sel" style="left:333px;top:130px;width:60px">6:00 pm</span>
    <span class="abs" style="left:19px;top:179px;width:379px;height:1px;background:#cfcfcf"></span>
    <span class="abs" style="left:320px;top:188px;width:74px;height:22px;background:var(--teal);color:#fff;font-family:'Jost',sans-serif;font-weight:600;font-size:10px;text-align:center;line-height:22px">NEXT</span>
  </div>
  <div class="tick" style="left:594px"><svg width="9" height="9" viewBox="0 0 9 9"><path d="M1 4.5l2.5 2.5L8 2" stroke="#fff" stroke-width="1.6" fill="none"/></svg></div>
  <div class="tick" style="left:616px"><svg width="9" height="9" viewBox="0 0 9 9"><path d="M1 4.5l2.5 2.5L8 2" stroke="#fff" stroke-width="1.6" fill="none"/></svg></div>
  <div class="tick" style="left:637px"><svg width="9" height="9" viewBox="0 0 9 9"><path d="M1 4.5l2.5 2.5L8 2" stroke="#fff" stroke-width="1.6" fill="none"/></svg></div>
  <div class="tick" style="left:660px"><svg width="9" height="9" viewBox="0 0 9 9"><path d="M1 4.5l2.5 2.5L8 2" stroke="#fff" stroke-width="1.6" fill="none"/></svg></div>
  <div class="tick" style="left:682px"><svg width="9" height="9" viewBox="0 0 9 9"><path d="M1 4.5l2.5 2.5L8 2" stroke="#fff" stroke-width="1.6" fill="none"/></svg></div>

  <!-- footer -->
  <footer class="site-footer"></footer>
  <div class="brand" style="left:310px;top:2604px;font-size:40px;line-height:54px">
    <span class="mark" style="width:50px;height:50px;display:block"></span>quarvendo
  </div>
  <nav class="footer-nav"><span>HOME</span><span>ABOUT</span><span>SERVICES</span><span>BLOGS</span><span>CONTACT</span></nav>
  <div class="social" aria-label="Social link" style="left:406px"></div>
  <div class="social" aria-label="Social link" style="left:441px"></div>
  <div class="social" aria-label="Social link" style="left:475px"></div>
  <div class="copyright">Copyright © 2025 quarvendo | Powered by quarvendo</div>

</div>
</body>
</html>
```